Real Estate Business Folders, Business Cards, Envelopes & Letterhead

Im looking for trendy, modern & professional design concepts for my business folder that will be used for real estate documents and property report presentations. I'm also looking for Business card designs, envelopes and letterhead with a similar theme. I have a logo already and I would like the logo colors to be incorporated in the design concepts.

Target Market(s)

Real Estate Investors, Banks, Financial Institutions

Industry/Entity Type

Real Estate

Colors
0455a3
959595
d3d3d3
848484

Requirements
Must have
• Trendy Modern, High Class look. Please include logo and colors and incorporate some silver or metallic.
• Business Address: 4127 Corvello Blvd ste 208-310
• N. Las Vegas, NV 89084
• Phone: 702-555-0187
• Fax : 702-555-0142
• Email: info@brookmerecastlesales.example
• Website: BrookmereCastleSales.example

```html
<!DOCTYPE html>
<html lang="en">
<head>
<meta charset="utf-8">
<title>Brookmere Castle Sales — Stationery Set</title>
<link rel="stylesheet" href="https://fonts.googleapis.com/css2?family=Montserrat:wght@400;500;600;700&display=swap">
<style>
  :root{
    --brand-blue:#0455a3;
    --silver:#959595;
    --light-silver:#d3d3d3;
    --mid-silver:#848484;
    --ink:#1c1c1e;
    --paper:#ffffff;
    --backdrop:#e6e7ea;
    --ghost:#eceef1;
  }
  *{box-sizing:border-box;margin:0;padding:0}
  html,body{width:1200px;height:3439px;overflow:hidden;background:var(--backdrop)}
  body{font-family:"Montserrat",Arial,sans-serif;color:var(--ink);position:relative}

  .section{position:absolute;left:0;width:1200px}
  .section--folders{top:0;height:672px}
  .section--cards{top:672px;height:768px}
  .section--envelope{top:1440px;height:648px}
  .section--letterhead{top:2088px;height:1351px}

  .sheet{position:absolute;background:var(--paper);overflow:hidden;box-shadow:0 2px 10px rgba(0,0,0,.12)}

  .brand{display:flex;align-items:center;gap:10px;position:absolute}
  .brand__mark{width:18px;height:18px;background:var(--brand-blue)}
  .brand__name{font-weight:700;color:var(--brand-blue);white-space:nowrap;letter-spacing:.02em}

  .mosaic{position:absolute}
  .mosaic--bold{background:linear-gradient(160deg,#0455a3 0%,#3a3f48 30%,#959595 55%,#0455a3 75%,#d3d3d3 100%)}
  .mosaic--faint{background:linear-gradient(200deg,#e7e9ed 0%,#f1f2f5 50%,#fbfbfc 100%)}

  /* Folders */
  .folder{top:56px;width:440px;height:560px}
  .folder--cover{left:140px}
  .folder--inside{left:620px}
  .folder--cover .mosaic--bold{right:0;top:0;width:200px;height:420px;clip-path:polygon(40% 0,100% 0,100% 100%,70% 80%,20% 55%,0 25%)}
  .folder--cover .mosaic--faint{left:0;top:40px;width:130px;height:360px;clip-path:polygon(0 0,60% 20%,100% 55%,40% 100%,0 100%)}
  .folder--cover .brand{left:36px;bottom:64px}
  .folder--cover .brand__name{font-size:17px}
  .folder--inside .mosaic--bold{right:0;bottom:0;width:190px;height:380px;clip-path:polygon(100% 0,100% 100%,10% 100%,0 70%,45% 35%)}
  .folder--inside .brand{left:36px;bottom:80px}
  .folder--inside .brand__name{font-size:17px}
  .folder__contact{position:absolute;left:36px;bottom:30px;font-size:8px;line-height:1.5;color:var(--mid-silver)}

  /* Cards */
  .card{top:230px;width:540px;height:309px}
  .card--front{left:620px}
  .card--back{left:40px}
  .card--front .brand{left:40px;top:70px}
  .card--front .brand__name{font-size:21px}
  .card--front .mosaic--bold{right:0;top:50px;width:270px;height:259px;clip-path:polygon(60% 0,100% 0,100% 100%,0 100%,25% 55%)}
  .card--back .mosaic--faint{right:0;top:0;width:230px;height:309px;clip-path:polygon(50% 0,100% 0,100% 100%,0 100%,20% 45%)}
  .card__accent{position:absolute;left:0;top:38px;width:16px;height:52px;background:var(--brand-blue)}
  .card__name{position:absolute;left:40px;top:40px;font-size:22px;font-weight:700}
  .card__role{position:absolute;left:40px;top:70px;font-size:13px;font-weight:600;color:var(--brand-blue)}
  .card__contact{position:absolute;left:40px;top:160px;font-size:13px;font-weight:700;line-height:1.45}
  .label{color:var(--brand-blue)}

  /* Envelope */
  .envelope{left:80px;top:100px;width:1040px;height:450px}
  .envelope .brand{left:36px;top:48px}
  .envelope .brand__name{font-size:20px}
  .envelope .mosaic--faint{right:0;top:0;width:360px;height:450px;clip-path:polygon(30% 0,100% 0,100% 100%,10% 100%,0 60%,20% 30%)}
  .envelope__return{position:absolute;left:36px;bottom:34px;font-size:13px;line-height:1.45}
  .envelope__return .lead{color:var(--brand-blue);font-weight:600}

  /* Letterhead */
  .letterhead{left:144px;top:90px;width:912px;height:1150px}
  .letterhead .brand{left:64px;top:70px}
  .letterhead .brand__name{font-size:22px}
  .letterhead .mosaic--faint{right:0;top:0;width:540px;height:1050px;clip-path:polygon(75% 0,100% 0,100% 100%,40% 100%,0 45%,30% 20%)}
  .letterhead__footer{position:absolute;left:64px;right:64px;bottom:54px;display:grid;grid-template-columns:1fr 1fr;column-gap:80px;row-gap:8px;font-size:15px}
  .footer-item{display:flex;align-items:flex-start;gap:12px;line-height:1.35}
  .footer-item svg{flex:none;margin-top:2px}
</style>
</head>
<body>

<section class="section section--folders">
  <div class="sheet folder folder--cover">
    <div class="mosaic mosaic--faint" role="img" aria-label="Faint silver triangle mosaic"></div>
    <div class="mosaic mosaic--bold" role="img" aria-label="Blue, grey and charcoal triangle mosaic"></div>
    <div class="brand"><span class="brand__mark"></span><span class="brand__name">Brookmere Castle Sales</span></div>
  </div>
  <div class="sheet folder folder--inside">
    <div class="mosaic mosaic--bold" role="img" aria-label="Blue, grey and charcoal triangle mosaic"></div>
    <div class="brand"><span class="brand__mark"></span><span class="brand__name">Brookmere Castle Sales</span></div>
    <p class="folder__contact">4127 Corvello Blvd ste 208-310, N. Las Vegas, NV 89084<br>Phone: 702-555-0187 | Email: info@brookmerecastlesales.example</p>
  </div>
</section>

<section class="section section--cards">
  <div class="sheet card card--back">
    <div class="mosaic mosaic--faint" role="img" aria-label="Faint silver triangle mosaic"></div>
    <span class="card__accent"></span>
    <p class="card__name">John Doe</p>
    <p class="card__role">Manager</p>
    <p class="card__contact">
      <span class="label">Address:</span> 4127 Corvello Blvd ste 208-310<br>
      N. Las Vegas, NV 89084<br>
      <span class="label">Phone:</span> 702-555-0187<br>
      <span class="label">Fax:</span> 702-555-0142<br>
      <span class="label">Email:</span> info@brookmerecastlesales.example<br>
      <span class="label">Website:</span> BrookmereCastleSales.example
    </p>
  </div>
  <div class="sheet card card--front">
    <div class="brand"><span class="brand__mark"></span><span class="brand__name">Brookmere Castle Sales</span></div>
    <div class="mosaic mosaic--bold" role="img" aria-label="Blue, grey and charcoal triangle mosaic"></div>
  </div>
</section>

<section class="section section--envelope">
  <div class="sheet envelope">
    <div class="mosaic mosaic--faint" role="img" aria-label="Faint silver triangle mosaic"></div>
    <div class="brand"><span class="brand__mark"></span><span class="brand__name">Brookmere Castle Sales</span></div>
    <p class="envelope__return">
      <span class="lead">If undelivered, please return to:</span><br>
      <span class="label">Address:</span> 4127 Corvello Blvd ste 208-310 N. Las Vegas, NV 89084<br>
      <span class="label">Phone:</span> 702-555-0187 | <span class="label">Fax</span> : 702-555-0142 | <span class="label">Email:</span> info@brookmerecastlesales.example<br>
      BrookmereCastleSales.example
    </p>
  </div>
</section>

<section class="section section--letterhead">
  <div class="sheet letterhead">
    <div class="mosaic mosaic--faint" role="img" aria-label="Faint silver triangle mosaic"></div>
    <div class="brand"><span class="brand__mark"></span><span class="brand__name">Brookmere Castle Sales</span></div>
    <div class="letterhead__footer">
      <div class="footer-item">
        <svg width="14" height="18" viewBox="0 0 14 18" aria-hidden="true"><path d="M7 0a7 7 0 0 0-7 7c0 5 7 11 7 11s7-6 7-11a7 7 0 0 0-7-7zm0 9.5A2.5 2.5 0 1 1 7 4.5a2.5 2.5 0 0 1 0 5z" fill="var(--brand-blue)"/></svg>
        <span>4127 Corvello Blvd ste 208-310<br>N. Las Vegas, NV 89084</span>
      </div>
      <div class="footer-item">
        <svg width="16" height="16" viewBox="0 0 16 16" aria-hidden="true"><path d="M3.5 1l2.5 3-1.5 2c1 2 3 4 5 5l2-1.5 3 2.5-1.5 3C7 15 1 9 1 2.5z" fill="var(--brand-blue)"/></svg>
        <span>702-555-0142</span>
      </div>
      <div class="footer-item">
        <svg width="16" height="12" viewBox="0 0 16 12" aria-hidden="true"><rect width="16" height="12" fill="var(--brand-blue)"/><path d="M0 0l8 6 8-6" fill="none" stroke="#fff" stroke-width="1.2"/></svg>
        <span>info@brookmerecastlesales.example</span>
      </div>
      <div class="footer-item">
        <svg width="16" height="16" viewBox="0 0 16 16" aria-hidden="true"><rect x="4" y="0" width="8" height="5" fill="var(--brand-blue)"/><rect x="0" y="5" width="16" height="7" fill="var(--brand-blue)"/><rect x="4" y="10" width="8" height="6" fill="var(--brand-blue)"/></svg>
        <span>702-555-0187</span>
      </div>
      <div class="footer-item" style="grid-column:2">
        <svg width="16" height="16" viewBox="0 0 16 16" aria-hidden="true"><circle cx="8" cy="8" r="7" fill="none" stroke="var(--brand-blue)" stroke-width="1.6"/><path d="M1 8h14M8 1c-3 3.5-3 10.5 0 14M8 1c3 3.5 3 10.5 0 14" fill="none" stroke="var(--brand-blue)" stroke-width="1.2"/></svg>
        <span>BrookmereCastleSales.example</span>
      </div>
    </div>
  </div>
</section>

</body>
</html>
```